Website design for Nutraceutical Contract Manufacturer in NJ

Develop website for a contract manufacturer, specializing in nutraceutical products. Our color theme is based on the colors of the American flag (Pantone blue no. 282 & red no. 193, white), representing a US presence of a company based in Italy. Our website will include a general e-mail box link for additional info. requests, color photos of our operation, a link to our parent company's website, a video, a mission statement, a description of our capabilities.Our internet presence will be on a B2B basis, to include a map of our location and contact information.

Target Market(s)

Businesses seeking contract manufacturer in the US nutraceutical industry.

Industry/Entity Type

Manufacturer

Number of Pages Required

3 page

Font styles to use
Sans Serif

Colors
3176b5
f04a50

Requirements
Must have
• Colors, as described in project description section. Three pages minimum - one to define what we do/location/contact info,/links to affiliated companies, one to showcase certifications, one to provide photos. We are open to having additional pages as suggested, if necessary. Our website for contacts info: www.veltracore-us.com .
• Link to our general email box: info@veltracore-us.com
• Pantone colors detailed in project description.
• HTTPS secure presence
Nice to have
• TBD
Should not have
• PROFANITY

```html
<!DOCTYPE html>
<html lang="en">
<head>
<meta charset="utf-8">
<title>Veltracore US – What We Do</title>
<link href="https://fonts.googleapis.com/css2?family=Montserrat:wght@600;700;800&family=Open+Sans:wght@400;600;700&display=swap" rel="stylesheet">
<style>
:root{
  --blue:#3176b5;
  --red:#c8102e;
  --sky:#d6ecf8;
  --search:#29a3dc;
  --ink:#2a2a2a;
  --muted:#777;
  --dark:#23262f;
  --band:#f5f6f7;
  --partner:#8a8a8a;
  --white:#fff;
}
*{margin:0;padding:0;box-sizing:border-box}
html,body{width:708px;height:1200px;overflow:hidden;background:var(--white)}
body{position:relative;font-family:"Open Sans",sans-serif;color:var(--ink)}
.abs{position:absolute}
.topbar{left:0;top:0;width:708px;height:22px;background:var(--sky)}
.topbar .item{top:4px;font-size:7px;color:#667;display:flex;align-items:center;gap:5px;text-transform:uppercase}
.icon-sq{width:14px;height:14px;background:var(--blue);display:inline-flex;align-items:center;justify-content:center}
.social{display:flex;gap:7px}
.social span,.fsocial span{background:var(--blue);display:flex;align-items:center;justify-content:center}
.social span{width:16px;height:16px}
.social span i,.fsocial span i{display:block;width:5px;height:5px;border-radius:50%;background:var(--white)}
.brand{font-family:"Open Sans",sans-serif;font-weight:700;color:var(--red);display:flex;align-items:center;gap:6px;line-height:1}
.brand .dot{background:var(--blue);border-radius:50%;display:block}
.contact-box{display:flex;gap:8px;align-items:flex-start}
.contact-box .ic{width:24px;height:24px;background:var(--blue);display:flex;align-items:center;justify-content:center;flex:none}
.contact-box .txt{line-height:10px;padding-top:2px}
.contact-box b{display:block;font-size:7px;font-weight:700;color:#444}
.contact-box small{display:block;font-size:7px;color:#777;margin-top:1px}
.nav{left:51px;top:73px;width:606px;height:35px;background:var(--blue);display:flex;align-items:center;padding-left:12px}
.nav a{font-family:"Montserrat",sans-serif;font-size:6px;font-weight:700;color:var(--white);text-decoration:none;padding:6px 5px;margin-right:3px;letter-spacing:.2px}
.nav a.active{background:var(--red);border-radius:2px}
.search{right:8px;top:6px;width:108px;height:23px;background:var(--search);color:#e6f4fb;font-size:7px;display:flex;align-items:center;justify-content:space-between;padding:0 8px}
.hero{left:0;top:108px;width:708px;height:208px;background:
  radial-gradient(ellipse 60px 40px at 80px 60px,#dfe6dc 0%,transparent 100%),
  radial-gradient(ellipse 40px 70px at 520px 170px,#c9cfe6 0%,transparent 100%),
  linear-gradient(180deg,#e9eef3 0%,#f4f6f8 55%,#e6ebf0 100%)}
.hero h1{left:59px;top:92px;font-family:"Montserrat",sans-serif;font-weight:800;font-size:17px;color:#222}
.hero p{left:59px;top:115px;font-size:7px;line-height:12px;color:#666}
.crumb{right:85px;top:118px;font-size:7px;font-weight:700;color:#555}
.section-title{left:0;width:708px;top:357px;text-align:center}
.section-title h2{font-family:"Montserrat",sans-serif;font-weight:700;font-size:12px;color:#222}
.section-title p{font-size:7px;line-height:12px;color:#777;margin-top:4px}
.card{width:288px;height:136px;display:flex;align-items:center;justify-content:center;font-family:"Montserrat",sans-serif;font-weight:700;font-size:10.5px;color:#2a2a2a;letter-spacing:.2px;border-radius:2px}
.tile-lab{background:
  radial-gradient(ellipse 70px 50px at 230px 40px,#efe7dc 0%,transparent 100%),
  radial-gradient(ellipse 120px 40px at 110px 120px,#d6d8db 0%,transparent 100%),
  linear-gradient(135deg,#eeeeef,#e6e7e9)}
.tile-consult{background:
  radial-gradient(ellipse 70px 110px at 240px 110px,#b9cbe6 0%,transparent 100%),
  radial-gradient(ellipse 90px 40px at 90px 50px,#dde4ec 0%,transparent 100%),
  linear-gradient(135deg,#f1f3f6,#e6ecf3)}
.tile-ward{background:
  radial-gradient(ellipse 80px 30px at 200px 115px,#aab6dd 0%,transparent 100%),
  radial-gradient(ellipse 90px 25px at 90px 100px,#e8e4d4 0%,transparent 100%),
  linear-gradient(180deg,#f0f1f3 0%,#e7e8eb 60%,#e1e3e8 100%)}
.tile-treat{background:
  radial-gradient(ellipse 140px 30px at 100px 12px,#cdbfb6 0%,transparent 100%),
  radial-gradient(ellipse 90px 60px at 140px 80px,#c9c9c9 0%,transparent 100%),
  linear-gradient(135deg,#e4e2df,#f2f1f0)}
.partners{left:0;top:916px;width:708px;height:57px;background:var(--band);border-top:1px solid #e6e6e6;display:flex;justify-content:space-around;align-items:center;padding:0 70px}
.badge{display:flex;flex-direction:column;align-items:center;gap:3px}
.badge i{display:block;background:var(--partner)}
.footer{left:0;top:973px;width:708px;height:227px;background:var(--dark)}
.footer h4{font-family:"Montserrat",sans-serif;font-weight:700;font-size:7.5px;color:var(--white)}
.footer .about{left:66px;top:88px;width:180px;font-size:7px;line-height:12px;color:#c8cbd2}
.footer .info{left:263px;top:72px;font-size:7px;line-height:12px;color:#c8cbd2;font-weight:600}
.fsocial{left:66px;top:129px;display:flex;gap:5px}
.fsocial span{width:20px;height:20px}
.subscribe{left:460px;top:53px;width:182px}
.subscribe .form{display:flex;margin-top:9px;height:25px}
.subscribe .form span{flex:1;background:#5b5f69;color:#ddd;font-size:6.5px;display:flex;align-items:center;padding-left:6px}
.subscribe .form b{width:54px;background:var(--blue);color:var(--white);font-size:6px;display:flex;align-items:center;justify-content:center}
.subscribe p{font-size:7px;line-height:12px;color:#c8cbd2;margin-top:5px}
.bottombar{left:51px;top:1171px;width:606px;height:29px;background:var(--blue);display:flex;justify-content:space-between;align-items:center;padding:6px 13px 0}
.bottombar small{font-size:6px;font-weight:700;color:var(--white)}
.bottombar nav{display:flex;gap:13px}
.totop{left:664px;top:1184px;width:18px;height:16px;background:var(--blue);color:var(--white);font-size:8px;text-align:center}
</style>
</head>
<body>

<div class="abs topbar">
  <div class="abs item" style="left:51px"><span class="icon-sq"><svg width="8" height="8" viewBox="0 0 8 8"><circle cx="4" cy="4" r="3.2" fill="none" stroke="#fff" stroke-width="1"/><line x1="0.8" y1="4" x2="7.2" y2="4" stroke="#fff" stroke-width=".8"/></svg></span>www.veltracore-us.com</div>
  <div class="abs item" style="left:160px"><span class="icon-sq"><svg width="7" height="9" viewBox="0 0 7 9"><path d="M3.5 9 L0.7 4.2 A3 3 0 1 1 6.3 4.2 Z" fill="#fff"/><circle cx="3.5" cy="3.2" r="1.1" fill="#3176b5"/></svg></span>info@veltracore-us.com</div>
  <div class="abs social" style="left:543px;top:3px"><span><i></i></span><span><i></i></span><span><i></i></span><span><i></i></span><span><i></i></span></div>
</div>

<div class="abs brand" style="left:58px;top:42px;font-size:18px"><span class="dot" style="width:8px;height:8px"></span>Veltracore US</div>

<div class="abs contact-box" style="left:431px;top:36px">
  <span class="ic"><svg width="12" height="12" viewBox="0 0 12 12"><path d="M2.5 1 L4.5 1 L5.3 3.6 L4 4.6 Q5 7 7.4 8 L8.4 6.7 L11 7.5 L11 9.5 Q10.5 11 9 11 Q1 10 1 2.5 Q1 1 2.5 1 Z" fill="#fff"/></svg></span>
  <div class="txt"><b>CALL US TODAY!</b><small>+1 (555) 014-2870</small></div>
</div>
<div class="abs contact-box" style="left:531px;top:36px">
  <span class="ic"><svg width="12" height="12" viewBox="0 0 12 12"><circle cx="6" cy="6" r="4.5" fill="none" stroke="#fff" stroke-width="1.3"/><path d="M6 3.5 V6 H8" stroke="#fff" stroke-width="1.2" fill="none"/></svg></span>
  <div class="txt"><b>EMAIL</b><small>INFO@VELTRACORE-US.COM</small></div>
</div>

<nav class="abs nav">
  <a href="#">HOME</a><a href="#">ABOUT</a><a href="#">GALLERY</a><a href="#" class="active">WHAT WE DO</a><a href="#">CERTIFICATES</a><a href="#">CONTACT</a>
  <div class="abs search">Search...<svg width="8" height="8" viewBox="0 0 8 8"><circle cx="3.3" cy="3.3" r="2.4" fill="none" stroke="#fff" stroke-width="1.1"/><line x1="5" y1="5" x2="7.5" y2="7.5" stroke="#fff" stroke-width="1.3"/></svg></div>
</nav>

<header class="abs hero" role="img" aria-label="Bright, softly blurred clinic corridor with reception desk">
  <h1 class="abs">WHAT WE DO</h1>
  <p class="abs">Lorem Ipsum is simply dummy text of the printing and typesetting industry.<br>It has survived not only five centuries</p>
  <div class="abs crumb">HOME <span style="color:#aaa;font-weight:400">&nbsp;/&nbsp;</span> WHAT WE DO</div>
</header>

<div class="abs section-title">
  <h2>WHAT WE DO</h2>
  <p>Lorem Ipsum is simply dummy text of the printing and typesetting industry.<br>It has survived not only five centuries</p>
</div>

<div class="abs card tile-lab" style="left:58px;top:419px" role="img" aria-label="Faded photo of laboratory testing equipment">LABORATORY TEST</div>
<div class="abs card tile-consult" style="left:362px;top:419px" role="img" aria-label="Faded photo of a doctor in blue scrubs">CONSULTATION</div>
<div class="abs card tile-ward" style="left:58px;top:571px" role="img" aria-label="Faded photo of a hospital ward with beds">EMERGENCY</div>
<div class="abs card tile-treat" style="left:362px;top:571px" role="img" aria-label="Faded photo of a treatment chair">TREATMENT</div>
<div class="abs card tile-ward" style="left:58px;top:723px" role="img" aria-label="Faded photo of a hospital ward with beds">MEDICINES</div>
<div class="abs card tile-ward" style="left:362px;top:723px" role="img" aria-label="Faded photo of a hospital ward with beds">PRODUCTION</div>

<div class="abs partners" aria-label="Partner badges">
  <div class="badge"><i style="width:13px;height:13px;border-radius:50%;background:none;border:2px solid var(--partner)"></i><i style="width:42px;height:3px"></i></div>
  <div class="badge"><i style="width:42px;height:5px"></i><i style="width:22px;height:2px"></i></div>
  <div class="badge" style="flex-direction:row;gap:4px"><i style="width:10px;height:10px;background:#444"></i><i style="width:50px;height:5px"></i></div>
  <div class="badge"><i style="width:46px;height:5px"></i><i style="width:18px;height:2px"></i></div>
  <div class="badge"><i style="width:58px;height:17px;background:none;border:1.5px solid #555"></i><i style="width:24px;height:2px"></i></div>
  <div class="badge"><i style="width:13px;height:13px;border-radius:50%;background:none;border:2px solid var(--partner)"></i><i style="width:42px;height:3px"></i></div>
</div>

<footer class="abs footer" role="contentinfo">
  <div class="abs" style="left:0;top:0;width:708px;height:227px;background:radial-gradient(ellipse at 50% 45%,#2b2f39 0%,var(--dark) 70%)" role="img" aria-label="Faint dotted world map background"></div>
  <div class="abs brand" style="left:66px;top:56px;font-size:21px;color:var(--red)"><span class="dot" style="width:9px;height:9px"></span>Veltracore US</div>
  <p class="abs about">Veltracore US LLC is a contract manufacturer for the food supplements market, producing exclusively for third parties.</p>
  <div class="abs fsocial"><span><i></i></span><span><i></i></span><span><i></i></span><span><i></i></span><span><i></i></span></div>
  <div class="abs" style="left:263px;top:55px"><h4>CONTACT INFO</h4></div>
  <p class="abs info">18 HARBOR LANE EASTON NJ 08000 USA<br>PHONE: +1 (555) 014-2870<br>EMAIL: INFO@VELTRACORE-US.COM<br>FAX: +1 (555) 014-2871</p>
  <div class="abs subscribe">
    <h4>SUBSCRIBE TO OUR CONTENTS</h4>
    <div class="form"><span>Email Address...</span><b>SUBSCRIBE</b></div>
    <p>There are design companies and then there are user experience design professional.</p>
  </div>
</footer>

<div class="abs bottombar">
  <small>© 2018 NORTHPEAK POWERED BY STUDIOLANE</small>
  <nav><small>ORDERS</small><small>TERMS</small><small>REPORT PROBLEM</small></nav>
</div>
<div class="abs totop">↑</div>

</body>
</html>
```